Business card for a plastic surgeon

i need a business card for a plastic surgeon. I have two adresses. The card should communicate safety, simmetry, beauty and with soft colors.
What i want in the card:
- my logo: Letters "R"and "B" (picture uploaded)
- my name: Renato Bastiani
- my registration: CRM 507 219
- my adresses and phone numbers (2):
- Av Dr Teixeira Lopes, 2710, sala 305 - Vila Serena | São Paulo/ SP - Phone: 11 4172-5036
- Al. Itapeva, 47, 3 andar - Jardim Aurora | Barueri/ SP - Phone: 11 6350-2481

- my social network: site, facebook and instagram

Target Market(s)

people (95% girls and women) that want cosmetic procedures and plastic surgery

Industry/Entity Type

Business

Contact Information for Business Card

The card should communicate safety, simmetry, beauty and with soft colors.
Beige, brown, gray, rosy are some options. Color is free

Font styles to use
Serif

Requirements
Must have
• - my logo: Letters "R"and "B" (picture uploaded)
• - my name: Renato Bastiani
• - my registration: CRM 507 219
• - my adresses and phone numbers (2):
• - Av Dr Teixeira Lopes, 2710, sala 305 - Vila Serena | São Paulo/ SP - Phone: 11 4172-5036
• - Al. Itapeva, 47, 3 andar - Jardim Aurora | Barueri/ SP - Phone: 11 6350-2481
• - my social network: site, facebook and instagram
Should not have
• other images (only my logo)

```html
<!DOCTYPE html>
<html lang="pt">
<head>
<meta charset="utf-8">
<title>Dr. Renato Bastiani — Cartão de visita</title>
<link rel="stylesheet" href="https://fonts.googleapis.com/css2?family=Cinzel:wght@400;500&family=Open+Sans:wght@400&display=swap">
<style>
  :root {
    --page-bg: #d9d2c8;
    --card-top: #f4f1ed;
    --card-bottom: #e6dfd7;
    --card-edge: #cfc6bb;
    --ink: #2b2a29;
    --ink-soft: #4a4542;
    --brown: #7a6152;
    --brown-dark: #5a4333;
    --band-dark: #1f1f22;
    --band-text: #d8cfc6;
  }
  html, body {
    margin: 0;
    width: 1200px;
    height: 1200px;
    overflow: hidden;
    background: var(--page-bg);
  }
  .card {
    position: absolute;
    left: 50px;
    top: 294px;
    width: 1100px;
    height: 612px;
    background: linear-gradient(180deg, var(--card-top), var(--card-bottom));
    border: 1px solid var(--card-edge);
    box-sizing: border-box;
    overflow: hidden;
    font-family: "Open Sans", Arial, sans-serif;
    color: var(--ink);
  }
  .brand {
    position: absolute;
    left: 58px;
    top: 120px;
    width: 360px;
    text-align: center;
  }
  .brand-mark {
    display: inline-flex;
    align-items: center;
    gap: 12px;
    font-family: "Cinzel", Georgia, serif;
    font-weight: 400;
    font-size: 34px;
    color: var(--brown);
  }
  .brand-mark .dot {
    width: 12px;
    height: 12px;
    border-radius: 50%;
    background: var(--brown);
  }
  .doctor-name {
    position: absolute;
    left: 58px;
    top: 232px;
    width: 360px;
    margin: 0;
    text-align: center;
    font-family: "Cinzel", Georgia, serif;
    font-weight: 400;
    font-size: 33px;
    color: var(--ink-soft);
    white-space: nowrap;
  }
  .specialty {
    position: absolute;
    left: 58px;
    top: 276px;
    width: 360px;
    margin: 0;
    text-align: center;
    font-family: "Cinzel", Georgia, serif;
    font-size: 16px;
    letter-spacing: 5px;
    color: var(--ink-soft);
  }
  .divider {
    position: absolute;
    left: 58px;
    top: 408px;
    width: 988px;
    height: 2px;
    background: var(--ink);
  }
  .contacts {
    position: absolute;
    left: 58px;
    top: 434px;
    margin: 0;
    padding: 0;
    list-style: none;
    font-size: 23px;
    line-height: 32.5px;
    color: var(--ink-soft);
  }
  .contacts li {
    display: flex;
    align-items: center;
    gap: 14px;
  }
  .contacts svg { width: 22px; height: 22px; fill: var(--brown); flex: none; }
  .addresses {
    position: absolute;
    right: 54px;
    top: 432px;
    text-align: right;
    font-size: 23px;
    line-height: 29px;
    color: var(--ink);
  }
  .addresses p { margin: 0 0 14px; }
  .footer-bands {
    position: absolute;
    left: 0;
    bottom: 0;
    width: 1100px;
    height: 40px;
  }
  .registration {
    position: absolute;
    right: 66px;
    bottom: 4px;
    margin: 0;
    font-size: 25px;
    line-height: 32px;
    color: var(--ink);
  }
  .registration .crm { color: var(--band-text); }
</style>
</head>
<body>
  <article class="card">
    <div class="brand">
      <span class="brand-mark"><span class="dot"></span>Bastiani</span>
    </div>
    <h1 class="doctor-name">DR. RENATO BASTIANI</h1>
    <p class="specialty">CIRURGIÃO PLÁSTICO</p>

    <div class="divider"></div>

    <ul class="contacts">
      <li>
        <svg viewBox="0 0 24 24" aria-hidden="true"><path d="M16 2c-5 1-11 7-11 13 0 4 2 7 4 7l3-4c-2-1-3-3-2-6s3-5 5-5l1-4z"/></svg>
        11 4172-5036
      </li>
      <li>
        <svg viewBox="0 0 24 24" aria-hidden="true"><path d="M16 2c-5 1-11 7-11 13 0 4 2 7 4 7l3-4c-2-1-3-3-2-6s3-5 5-5l1-4z"/></svg>
        11 6350-2481
      </li>
      <li>
        <svg viewBox="0 0 24 24" aria-hidden="true"><path d="M2 5h20v14H2z M2 5l10 8 10-8" fill="none" stroke="#7a6152" stroke-width="2"/><path d="M2 5h20l-10 8z"/></svg>
        info@bastianiclinica.com
      </li>
      <li>
        <svg viewBox="0 0 24 24" aria-hidden="true"><circle cx="12" cy="12" r="9" fill="none" stroke="#7a6152" stroke-width="2"/><path d="M3 12h18M12 3c-4 5-4 13 0 18M12 3c4 5 4 13 0 18" fill="none" stroke="#7a6152" stroke-width="1.5"/></svg>
        www.bastianiclinica.com
      </li>
    </ul>

    <div class="addresses">
      <p>Al. Itapeva, 47, 3 andar -<br>Jardim Aurora Barueri/ SP</p>
      <p>Av Dr Teixeira Lopes, 2710, sala<br>305 - Vila Serena São Paulo/ SP</p>
    </div>

    <svg class="footer-bands" viewBox="0 0 1100 40" aria-hidden="true">
      <polygon points="0,16 630,16 608,40 0,40" fill="var(--band-dark)"/>
      <polygon points="648,0 1100,0 1100,40 614,40" fill="var(--brown-dark)"/>
    </svg>
    <p class="registration">registration: <span class="crm">CRM 507 219</span></p>
  </article>
</body>
</html>
```